Business card for Real Estate Company located in Coastal area of spain

Want a business card design. Simple, professional, horizontal layout. will be 2 sided. Name of company (logo big on front). Name of agent, phone and email address. Back side will be list of general services we provide. Would like to see 2 separate concepts using the 2 separate logo treatments. One using Rich dark, bright blue as the stock color, and the other using White as the stock color.
Logo files uploaded (2 different versions) Domain (harbourkeyestates.com) Moraira-Calpe-Altea-Javea-Denia-Marina Alta Area (perhaps across the bottom of the front of card0 Ingrid Tavel Licensed Estate Agent / Partner Ingrid@harbourkeyestates.com +34.611.48.27.09 Back of card should list services offered

Real Estate Sales and Investments Real Estate Rental Management Kitchen, Bathroom Reformations Complete Home Reformation Services Window and Door Replacement Landscape and Garden Management Pool and Jacuzzi Service

Target Market(s)

Real estate and construction

Industry/Entity Type

Real Estate

Contact Information for Business Card

Logo files uploaded (2 different versions) Domain (harbourkeyestates.com) Moraira-Calpe-Altea-Javea-Denia-Marina Alta Area (perhaps across the bottom of the front of card0 Ingrid Tavel Licensed Estate Agent / Partner Ingrid@harbourkeyestates.com +34.611.48.27.09

Colors

Designer to choose colors to be used in the design.

Requirements
Must have
• progressive look professional
Nice to have
• Front big logo, Agent details. Back, list of services included in project description
Should not have
• Gloss finish for card

```html
<!DOCTYPE html>
<html lang="en">
<head>
<meta charset="utf-8">
<title>Harbour Key Estates – Business Card</title>
<link href="https://fonts.googleapis.com/css2?family=Lato:wght@300;400;700;900&display=swap" rel="stylesheet">
<style>
  :root {
    --bg: #1e1e22;
    --card-white: #ffffff;
    --brand-blue: #4a63dd;
    --brand-violet: #7b5fcf;
    --brand-purple: #ad68b8;
    --ink: #3a3a44;
    --on-dark: #ffffff;
  }
  * { box-sizing: border-box; margin: 0; padding: 0; }
  html, body { width: 1200px; height: 800px; overflow: hidden; }
  body {
    background: var(--bg);
    font-family: "Lato", sans-serif;
    display: flex;
    align-items: center;
    justify-content: center;
    gap: 40px;
  }
  .card {
    position: relative;
    width: 560px;
    height: 320px;
    border-radius: 18px;
    overflow: hidden;
  }

  /* ---------- front ---------- */
  .card-front { background: var(--card-white); }
  .front-band { position: absolute; inset: 0; }
  .wordmark {
    position: absolute;
    left: 36px; top: 38px;
    font-weight: 300;
    font-size: 44px;
    letter-spacing: 0.5px;
    color: var(--brand-violet);
  }
  .agent {
    position: absolute;
    left: 40px; top: 118px;
  }
  .agent-name {
    font-weight: 900;
    font-size: 26px;
    letter-spacing: 0.5px;
    text-transform: uppercase;
    color: var(--brand-blue);
  }
  .agent-title {
    margin-top: 2px;
    font-size: 14px;
    color: var(--brand-purple);
  }
  .divider {
    position: absolute;
    left: 262px; top: 120px;
    width: 1.5px; height: 54px;
    background: var(--brand-violet);
  }
  .contact {
    position: absolute;
    left: 278px; top: 118px;
    list-style: none;
    font-size: 12.5px;
    color: var(--ink);
    line-height: 19px;
  }
  .contact li { display: flex; align-items: center; gap: 8px; }
  .contact svg { width: 11px; height: 11px; fill: var(--brand-blue); flex: none; }
  .service-area {
    position: absolute;
    right: 24px; bottom: 20px;
    display: flex; align-items: center; gap: 6px;
    font-size: 12px;
    color: var(--on-dark);
    letter-spacing: 0.3px;
  }
  .service-area svg { width: 10px; height: 12px; fill: var(--on-dark); }

  /* ---------- back ---------- */
  .card-back {
    background: linear-gradient(100deg, var(--brand-blue) 0%, var(--brand-violet) 45%, var(--brand-purple) 100%);
  }
  .back-band {
    position: absolute; left: 0; top: 0;
    width: 140px; height: 320px;
    background: var(--brand-blue);
    border-right: 2px solid rgba(255, 255, 255, 0.35);
  }
  .back-wordmark {
    position: absolute;
    left: 70px; top: 160px;
    transform: translate(-50%, -50%) rotate(90deg);
    white-space: nowrap;
    font-weight: 300;
    font-size: 27px;
    color: var(--on-dark);
  }
  .services {
    position: absolute;
    left: 172px; top: 52px;
    list-style: none;
    color: var(--on-dark);
    font-size: 16px;
    letter-spacing: 0.4px;
  }
  .services li { display: flex; align-items: center; gap: 12px; height: 30px; }
  .services svg { width: 15px; height: 15px; flex: none; }
</style>
</head>
<body>

  <!-- Front -->
  <section class="card card-front">
    <svg class="front-band" viewBox="0 0 560 320" preserveAspectRatio="none" aria-hidden="true">
      <defs>
        <linearGradient id="frontBand" x1="0" y1="1" x2="1" y2="0">
          <stop offset="0" stop-color="#4a63dd"/>
          <stop offset="0.55" stop-color="#7b5fcf"/>
          <stop offset="1" stop-color="#ad68b8"/>
        </linearGradient>
      </defs>
      <polygon points="0,262 560,186 560,320 0,320" fill="url(#frontBand)"/>
      <line x1="0" y1="254" x2="560" y2="178" stroke="#ad68b8" stroke-width="1.2" opacity="0.7"/>
    </svg>

    <div class="wordmark">harbourkeyestates.com</div>

    <div class="agent">
      <div class="agent-name">Ingrid Tavel</div>
      <div class="agent-title">Licensed Estate Agent / Partner</div>
    </div>

    <div class="divider"></div>

    <ul class="contact">
      <li><svg viewBox="0 0 24 24"><path d="M6.6 10.8a15.1 15.1 0 0 0 6.6 6.6l2.2-2.2a1 1 0 0 1 1-.25 11.4 11.4 0 0 0 3.6.57 1 1 0 0 1 1 1V20a1 1 0 0 1-1 1A17 17 0 0 1 3 4a1 1 0 0 1 1-1h3.5a1 1 0 0 1 1 1c0 1.25.2 2.45.57 3.57a1 1 0 0 1-.25 1z"/></svg>+34.611.48.27.09</li>
      <li><svg viewBox="0 0 24 24"><path d="M2 5h20v14H2z M2 5l10 8 10-8" stroke="#fff" stroke-width="1.5"/></svg>Ingrid@harbourkeyestates.com</li>
      <li><svg viewBox="0 0 24 24"><circle cx="12" cy="12" r="10"/></svg>harbourkeyestates.com</li>
    </ul>

    <div class="service-area">
      <svg viewBox="0 0 20 24"><path d="M10 0a8 8 0 0 0-8 8c0 6 8 16 8 16s8-10 8-16a8 8 0 0 0-8-8zm0 11a3 3 0 1 1 0-6 3 3 0 0 1 0 6z"/></svg>
      Marina Alta Area — Moraira · Calpe · Altea · Javea · Denia
    </div>
  </section>

  <!-- Back -->
  <section class="card card-back">
    <div class="back-band" aria-hidden="true"></div>
    <div class="back-wordmark">harbourkeyestates.com</div>

    <ul class="services">
      <li><svg viewBox="0 0 16 16"><circle cx="8" cy="8" r="8" fill="#fff"/><path d="M4.5 8.2l2.3 2.3 4.7-4.7" fill="none" stroke="#6a5fd6" stroke-width="1.8"/></svg>Real Estate Sales and Investments</li>
      <li><svg viewBox="0 0 16 16"><circle cx="8" cy="8" r="8" fill="#fff"/><path d="M4.5 8.2l2.3 2.3 4.7-4.7" fill="none" stroke="#6a5fd6" stroke-width="1.8"/></svg>Real Estate Rental Management</li>
      <li><svg viewBox="0 0 16 16"><circle cx="8" cy="8" r="8" fill="#fff"/><path d="M4.5 8.2l2.3 2.3 4.7-4.7" fill="none" stroke="#6a5fd6" stroke-width="1.8"/></svg>Kitchen, Bathroom Reformations</li>
      <li><svg viewBox="0 0 16 16"><circle cx="8" cy="8" r="8" fill="#fff"/><path d="M4.5 8.2l2.3 2.3 4.7-4.7" fill="none" stroke="#6a5fd6" stroke-width="1.8"/></svg>Complete Home Reformation Services</li>
      <li><svg viewBox="0 0 16 16"><circle cx="8" cy="8" r="8" fill="#fff"/><path d="M4.5 8.2l2.3 2.3 4.7-4.7" fill="none" stroke="#6a5fd6" stroke-width="1.8"/></svg>Window and Door Replacement</li>
      <li><svg viewBox="0 0 16 16"><circle cx="8" cy="8" r="8" fill="#fff"/><path d="M4.5 8.2l2.3 2.3 4.7-4.7" fill="none" stroke="#6a5fd6" stroke-width="1.8"/></svg>Landscape and Garden Management</li>
      <li><svg viewBox="0 0 16 16"><circle cx="8" cy="8" r="8" fill="#fff"/><path d="M4.5 8.2l2.3 2.3 4.7-4.7" fill="none" stroke="#6a5fd6" stroke-width="1.8"/></svg>Pool and Jacuzzi Service</li>
    </ul>
  </section>

</body>
</html>
```